Glostiva: Graphic elements & webpage layout

Hi there! We’re building a site called Glostiva.example—it will be a community site for beauty product reviews, product recommendations and beauty tutorials. We've already got a logo, thanks to another CraftHive project. This project on CraftHive involves the following web design work:

1) Propose the overall graphic design elements of our site (according to our guidelines, which are in the attached file)

-Color Palette
-Fonts
-Icon set(s)

2) Using the overall graphic design elements in step 1 and our storyboard (attached), develop a webpage layout for the "How-to" page of our site. The "How-to" pages will be an editorial format, where our beauty journalist will show a video (and photos) of step-by-step beauty tutorials.

Please take a look at the attached files for a detailed brief and the logo! Thanks and we're looking forward to working with you!

Target Market(s)

Glostiva is for a French, English, and American audience of women between the ages of 16 and 30, who buy and use beauty products regularly.

Industry/Entity Type

Graphic Design

Requirements
Must have
• 1) A global set of graphic standards for the website Glostiva.example:
• A color palette
• Fonts
• An icon set (or sets)
• A menu
• Other graphic elements like button styles

2) A webpage layout (non-coded) for the How-To page template
(See storyboard, attached separately)
This webpage layout is for the main editorial format on Glostiva—step by step beauty tutorials. The individual on-page elements are in the storyboard, but overall we’d like it to look clean, friendly, and to encourage community participation and sharing on social networks.
Nice to have
• • A look and feel that is fresh, clean and modern
• Proximity: Establishes a close proximity with the user. (We want them to get the same feeling they get when talking beauty tips with their close friends).
• Neutrality: A sincere and neutral look and feel that doesn’t suggest a preference for any particular or elite type of beauty (but it can still be fun!)
• The graphic design is relevant to the beauty sector as a whole. (We could be talking about lipstick, a hairbrush or a man’s cologne)
• The graphic design alludes to the beauty industry (discreetly, not overtly!)
Should not have
• We've already got a logo, so you shouldn't suggest a new one!

We really want to avoid designs that are too traditionally "beauty" or too girly and feminine. Please no pink, no flowers, etc! :)

```html
<!DOCTYPE html>
<html lang="fr">
<head>
<meta charset="utf-8">
<title>Glostiva – Titre du tutorial</title>
<link href="https://fonts.googleapis.com/css2?family=Marcellus&family=Open+Sans:wght@400;600;700&display=swap" rel="stylesheet">
<style>
:root{
  --orange:#f7941d;
  --orange-dark:#e07e0c;
  --teal:#4fc3a1;
  --teal-soft:#e2f5ee;
  --teal-line:#b7e4d5;
  --peach-soft:#fdf0df;
  --peach-line:#f3d4ac;
  --ink:#3f3f3f;
  --muted:#8a8a8a;
  --line:#dcdcdc;
  --paper:#ffffff;
}
*{box-sizing:border-box;margin:0;padding:0}
html,body{width:1200px;height:2500px;overflow:hidden}
body{background:var(--paper);font-family:"Open Sans",Arial,sans-serif;color:var(--ink);position:relative;font-size:15px;line-height:1.45}
.abs{position:absolute}
.topbar{left:0;top:0;width:1200px;height:22px;background:var(--teal-soft);border-bottom:1px solid var(--teal-line)}
.topbar .links{position:absolute;right:120px;top:3px;font-size:11px;color:var(--ink);display:flex;gap:16px}
.topbar .links span::before{content:"";display:inline-block;width:9px;height:9px;background:var(--teal);margin-right:5px;vertical-align:-1px}
.brand{left:120px;top:42px;font-weight:700;font-size:60px;color:var(--ink);letter-spacing:-1px;display:flex;align-items:center;gap:12px}
.brand i{display:block;width:18px;height:18px;border-radius:50%;background:var(--teal)}
.nav{right:120px;top:84px;display:flex;align-items:center;gap:18px;font-size:16px}
.search{display:flex;gap:8px}
.search .field{width:200px;height:28px;border:1px solid var(--line);background:#fff}
.search .btn{width:64px;height:28px;background:var(--teal);color:#fff;font-size:11px;display:flex;align-items:center;justify-content:center}
.band{left:0;top:175px;width:1200px;height:430px;background:var(--orange)}
.title{left:120px;top:182px;font-family:"Marcellus",Georgia,serif;color:#fff;font-size:44px;letter-spacing:1px;line-height:1.2}
.meta{left:120px;top:240px;color:#fff;font-size:15px;display:flex;gap:14px;align-items:center}
.stars{letter-spacing:2px}
.share{left:700px;top:238px;display:flex;gap:6px}
.share i{width:20px;height:20px;background:#fff;opacity:.9;border-radius:3px}
.card{background:#fff;border:1px solid var(--line)}
.video-card{left:120px;top:270px;width:660px;height:490px;padding:16px}
.media{width:100%;position:relative}
.play{position:absolute;left:50%;top:50%;transform:translate(-50%,-50%)}
.controls{height:26px;background:#ececec;border-top:1px solid #d2d2d2;display:flex;align-items:center;gap:10px;padding:0 10px;font-size:10px;color:var(--muted)}
.controls .track{flex:1;height:4px;background:#cfcfcf}
p.lorem{font-size:15px;line-height:1.45;color:var(--ink)}
.aside-box{left:800px;top:265px;width:280px;height:475px;background:#fff;border:1px solid var(--line);padding:14px 18px}
.aside-box h3{font-family:"Marcellus",Georgia,serif;font-weight:400;font-size:30px;line-height:1.05;margin-bottom:14px}
.aside-box ul{list-style:none}
.aside-box li{font-size:13px;padding:10px 0 10px 18px;border-top:1px solid #eee;position:relative}
.aside-box li::before{content:"";position:absolute;left:2px;top:17px;width:7px;height:7px;background:var(--orange)}
h2.step{font-family:"Marcellus",Georgia,serif;font-weight:400;font-size:42px;color:var(--ink);letter-spacing:1px;line-height:1.2}
.tabbox{background:var(--teal-soft);border:1px solid var(--teal-line);padding:10px 14px 14px}
.tabbox.warm{background:var(--peach-soft);border-color:var(--peach-line)}
.tabs{display:flex;gap:4px;margin-bottom:8px}
.tab{width:88px;height:26px;font-size:12px;font-weight:600;display:flex;align-items:center;justify-content:center;background:#cfeee3;color:var(--ink)}
.tab.on{background:#fff;border:1px solid var(--teal-line)}
.warm .tab{background:#f7dcb8}
.warm .tab.on{background:#fff;border-color:var(--peach-line)}
.product{display:flex;gap:12px;height:86px}
.thumb{width:70px;height:76px;flex:none}
.product h4{font-size:14px;font-weight:600;margin-top:4px;line-height:1.3}
.product small{display:block;font-size:10px;color:var(--muted)}
.buy{display:inline-block;margin-top:6px;background:var(--orange);color:#fff;font-size:11px;padding:3px 10px}
.grid{display:grid;grid-template-columns:repeat(2,minmax(0,1fr));column-gap:12px;row-gap:26px}
.grid .product{height:112px;gap:8px;min-width:0}
.grid .product > div:last-child{min-width:0}
.grid .thumb{width:50px;height:58px}
.grid .product h4{font-size:12px;margin-top:0}
.grid .buy{padding:3px 8px;font-size:10px}
.arrow{position:absolute;top:50%;width:26px;height:26px;background:#fff;border-radius:50%;transform:translateY(-50%);display:flex;align-items:center;justify-content:center}
.form{left:120px;top:2075px;width:660px}
.row{display:flex;align-items:center;margin-bottom:12px;font-size:12px}
.row label{width:180px}
.row .field{flex:1;height:30px;border:1px solid var(--line);background:#fafafa}
.textarea{height:90px;border:1px solid var(--line);background:#fafafa;font-size:12px;padding:6px 10px;color:var(--muted)}
.submit{float:right;margin-top:10px;background:var(--orange);color:#fff;font-size:12px;padding:6px 22px}
.byline{font-size:11px;color:var(--muted);margin-top:8px}
.footer{left:0;top:2440px;width:1200px;height:60px;background:var(--teal-soft);border-top:1px solid var(--teal-line);display:flex;align-items:center;justify-content:center;font-size:12px;gap:8px}
</style>
</head>
<body>

<div class="abs topbar"><div class="links"><span>Choix de la langue</span><span>Chirpa</span><span>Amisphere</span></div></div>

<div class="abs brand"><i></i>Glostiva</div>
<div class="abs nav"><span>How to</span><span>Tips</span><div class="search"><div class="field"></div><div class="btn">search</div></div></div>

<div class="abs band"></div>
<div class="abs title">TITRE DU TUTORIAL</div>
<div class="abs meta"><span>Difficulté <span class="stars">★★★★☆</span></span><span>|</span><span>Durée: 20 minutes</span><span>|</span><span>Occasion: Soirée</span></div>
<div class="abs share"><i></i><i></i><i></i></div>

<section class="abs card video-card">
  <div class="media" style="height:330px;background:linear-gradient(135deg,#6b7f4e,#c27a2a 45%,#3d3a2c)" role="img" aria-label="Vidéo du tutorial : papillon orange sur des fleurs">
    <svg class="play" width="64" height="64" viewBox="0 0 64 64"><circle cx="32" cy="32" r="30" fill="#000" opacity=".55"/><path d="M26 20 L46 32 L26 44Z" fill="#fff"/></svg>
  </div>
  <div class="controls"><span>▶</span><span>0:00</span><div class="track"></div><span>2:30</span><span>⛶</span></div>
  <p class="lorem" style="margin-top:12px">Lorem ipsum dolor sit amet, maiores ornare ac fermentum, imperdiet ut vivamus a,nam lectus at nunc. Quam euismod sem, semper ut potenti pellentesque quisque.In eget sapien sed, sit duis vestibulum ultricies, placerat morbi amet vel, nullam in lorem vel.</p>
</section>

<aside class="abs aside-box">
  <h3>Les produits nécessaires</h3>
  <ul>
    <li>Lorem ipsum dolor</li>
    <li>sit amet consectetur</li>
    <li>Proin iaculis massa</li>
    <li>Sollicitudin enim bibendum</li>
    <li>Etiam imperdiet metus</li>
    <li>Quis ligula gravida</li>
    <li>Elementum</li>
    <li>Morbi accumsan</li>
    <li>Sollicitudin et sodales eu</li>
  </ul>
</aside>

<h2 class="abs step" style="left:120px;top:790px">ETAPE 1</h2>
<section class="abs tabbox" style="left:120px;top:845px;width:660px;height:445px">
  <div class="tabs"><div class="tab on">Vidéo</div><div class="tab">Photos</div></div>
  <div class="media" style="height:355px;background:linear-gradient(120deg,#2c2c2c,#7a6d68 50%,#1f1f1f)" role="img" aria-label="Vidéo de l'étape 1 : démonstration face caméra">
    <svg class="play" width="64" height="64" viewBox="0 0 64 64"><circle cx="32" cy="32" r="30" fill="#000" opacity=".55"/><path d="M26 20 L46 32 L26 44Z" fill="#fff"/></svg>
  </div>
  <div class="controls"><span>▶</span><span>0:00</span><div class="track"></div><span>1:45</span><span>⛶</span></div>
</section>
<p class="abs lorem" style="left:120px;top:1302px;width:660px">Lorem ipsum dolor sit amet, maiores ornare ac fermentum, imperdiet ut vivamus a,nam lectus at nunc. Quam euismod sem, semper ut potenti pellentesque quisque.In eget sapien sed, sit duis vestibulum ultricies, placerat morbi amet vel, nullam in lorem vel.</p>

<div class="abs" style="left:808px;top:840px;width:272px">
  <div class="product"><div class="thumb" style="background:linear-gradient(#d8d8d8,#9a9a9a)" role="img" aria-label="Flacon de produit"></div><div><h4>Donec tellus enim</h4><small>Voulez-vous en plus</small><span class="buy">Acheter</span></div></div>
  <div class="product"><div class="thumb" style="background:linear-gradient(#f0e6da,#c9b79f)" role="img" aria-label="Tube de crème"></div><div><h4>Pellentesque vitae metus</h4><small>Voulez-vous en plus</small><span class="buy">Acheter</span></div></div>
  <div class="product"><div class="thumb" style="background:linear-gradient(#e9e2ea,#a898a8)" role="img" aria-label="Flacon de soin"></div><div><h4>Aliquam imperdiet</h4><small>Voulez-vous en plus</small><span class="buy">Acheter</span></div></div>
  <div class="product"><div class="thumb" style="background:linear-gradient(#b23a3a,#5a1d1d)" role="img" aria-label="Rouges à lèvres"></div><div><h4>Maecenas ullamcorper</h4><small>Voulez-vous en plus</small><span class="buy">Acheter</span></div></div>
  <div class="product"><div class="thumb" style="background:linear-gradient(#f2d9a8,#b8894a)" role="img" aria-label="Parfums"></div><div><h4>Aenean placerat urna</h4><small>Voulez-vous en plus</small><span class="buy">Acheter</span></div></div>
  <div class="product"><div class="thumb" style="background:linear-gradient(#e8e0c8,#a79c78)" role="img" aria-label="Flacons de lotion"></div><div><h4>Nullam volutpat tempor</h4><small>Voulez-vous en plus</small><span class="buy">Acheter</span></div></div>
</div>

<h2 class="abs step" style="left:120px;top:1405px">ETAPE 2</h2>
<section class="abs tabbox warm" style="left:120px;top:1460px;width:660px;height:440px">
  <div class="tabs"><div class="tab on">Photos</div><div class="tab">Vidéo</div></div>
  <div class="media" style="height:385px;background:linear-gradient(110deg,#f3ece6,#e2c2a8 55%,#f6f1ec)" role="img" aria-label="Photo de l'étape 2 : portrait beauté, peau lumineuse">
    <div class="arrow" style="left:10px"><svg width="10" height="12" viewBox="0 0 10 12"><path d="M8 1 L2 6 L8 11" stroke="#555" stroke-width="2" fill="none"/></svg></div>
    <div class="arrow" style="right:10px"><svg width="10" height="12" viewBox="0 0 10 12"><path d="M2 1 L8 6 L2 11" stroke="#555" stroke-width="2" fill="none"/></svg></div>
  </div>
</section>
<p class="abs lorem" style="left:120px;top:1912px;width:660px">Lorem ipsum dolor sit amet, maiores ornare ac fermentum, imperdiet ut vivamus a,nam lectus at nunc. Quam euismod sem, semper ut potenti pellentesque quisque.In eget sapien sed, sit duis vestibulum ultricies, placerat morbi amet vel, nullam in lorem vel.</p>

<div class="abs grid" style="left:808px;top:1460px;width:272px">
  <div class="product"><div class="thumb" style="background:linear-gradient(#2d2d2d,#777)" role="img" aria-label="Palette de maquillage"></div><div><h4>Donec tellus enim</h4><small>Voulez-vous en plus</small><span class="buy">Acheter</span></div></div>
  <div class="product"><div class="thumb" style="background:linear-gradient(#f3e1d3,#c9a183)" role="img" aria-label="Produit de soin"></div><div><h4>Nulla accumsan</h4><small>Voulez-vous en plus</small><span class="buy">Acheter</span></div></div>
  <div class="product"><div class="thumb" style="background:linear-gradient(#e6dde8,#a68fae)" role="img" aria-label="Flacon violet"></div><div><h4>Donec vestibulum</h4><small>Voulez-vous en plus</small><span class="buy">Acheter</span></div></div>
  <div class="product"><div class="thumb" style="background:linear-gradient(#eee,#aaa)" role="img" aria-label="Pinceaux"></div><div><h4>Nullam blandit</h4><small>Voulez-vous en plus</small><span class="buy">Acheter</span></div></div>
  <div class="product"><div class="thumb" style="background:linear-gradient(#e7d9bf,#a88d5c)" role="img" aria-label="Flacons de parfum"></div><div><h4>Pellentesque vitae</h4><small>Voulez-vous en plus</small><span class="buy">Acheter</span></div></div>
  <div class="product"><div class="thumb" style="background:linear-gradient(#444,#111)" role="img" aria-label="Mascara"></div><div><h4>Mauris velit nisi</h4><small>Voulez-vous en plus</small><span class="buy">Acheter</span></div></div>
</div>

<h2 class="abs step" style="left:120px;top:2015px">COMMENTAIRES (12)</h2>
<form class="abs form">
  <div class="row"><label>Nom</label><div class="field"></div></div>
  <div class="row"><label>Mail (n'apparaîtra pas)</label><div class="field"></div></div>
  <div class="textarea">Laissez votre commentaire ici !</div>
  <span class="submit">Commenter</span>
</form>
<div class="abs" style="left:120px;top:2330px;width:660px">
  <p class="lorem" style="font-size:13px">Lorem ipsum dolor sit amet, maiores ornare ac fermentum, imperdiet ut vivamus a,nam lectus at nunc. Quam euismod sem, semper ut potenti pellentesque quisque.In eget sapien sed, sit duis vestibulum.</p>
  <p class="byline">Commentaire de <b style="color:var(--ink)">Léa Marlin</b> posté le <b style="color:var(--ink)">24th June 2011</b></p>
</div>

<footer class="abs footer"><span>How-to</span>|<span>Tips</span>|<span>copyright 2011 · Glostiva · All rights reserved</span></footer>

</body>
</html>
```